Kestwell Finanz AG needs web design

We need a website for a Swiss company: Kestwell Finanz AG. We offer our customers financial services such as advice and funds. We also have an interest rate calculator that we want to link to via a button on the website.

We are looking for a black and gold design. (Background: Black, Accents: Gold and White)
The design should convey security and growth. We have uploaded our logo in the attachment.
Font from the logo: Trajan Pro Regular

```html
<!DOCTYPE html>
<html lang="en">
<head>
<meta charset="utf-8">
<title>Kestwell Finanz AG</title>
<link href="https://fonts.googleapis.com/css2?family=Cinzel:wght@400;600&family=Poppins:wght@400;500&display=swap" rel="stylesheet">
<style>
:root{
  --black:#060606;
  --panel:#1b1b1b;
  --white:#ffffff;
  --grey:#d9d9d9;
  --gold:#c9a55a;
  --gold-light:#f1d9a0;
  --gold-dark:#8a6a2c;
  --gold-grad:linear-gradient(90deg,#9b7a3a 0%,#e9cf8f 50%,#a9843f 100%);
  --serif:'Cinzel',serif;
  --sans:'Poppins',sans-serif;
}
*{margin:0;padding:0;box-sizing:border-box}
html,body{width:1200px;height:5111px;overflow:hidden;background:var(--black)}
body{position:relative;font-family:var(--sans);color:var(--white)}
.abs{position:absolute}
.btn{position:absolute;display:flex;align-items:center;justify-content:center;border-radius:30px;background:var(--gold-grad);color:#2a1e08;font-family:var(--serif);letter-spacing:1px}
.rule{position:absolute;height:5px;display:flex;gap:16px}
.rule span{flex:1;background:var(--gold-grad);clip-path:polygon(0 60%,100% 0,100% 100%,0 100%)}
.rule span:last-child{clip-path:polygon(0 0,100% 60%,100% 100%,0 100%)}
.heading{position:absolute;font-family:var(--serif);font-size:64px;line-height:1;color:var(--white);letter-spacing:1px}
.lede{position:absolute;font-size:14px;line-height:22px;color:var(--grey)}
.photo{position:absolute}

/* header */
.brand{left:160px;top:18px;width:220px;text-align:center;font-family:var(--serif);font-size:20px;color:var(--gold);line-height:26px}
.brand .mark{display:block;margin:0 auto 6px;width:40px;height:40px;border:2px solid var(--gold)}
.nav{left:440px;top:84px;display:flex;gap:26px;font-family:var(--serif);font-size:15px}
.nav a{color:var(--white);text-decoration:none}
.nav a.active{border-bottom:2px solid var(--gold);padding-bottom:6px}
.topbar{left:656px;top:22px;display:flex;align-items:center;gap:14px;font-size:20px}
.social{display:flex;gap:14px}
.social i{display:block;width:34px;height:34px;border-radius:50%;background:var(--gold)}

/* hero */
.hero-photo{left:0;top:0;width:1200px;height:740px;background:radial-gradient(ellipse at 30% 40%,#5a4d3e 0%,#2b2520 45%,#0b0b0b 80%)}
.hero-fade{left:0;top:560px;width:1200px;height:240px;background:linear-gradient(180deg,rgba(6,6,6,0) 0%,#060606 75%)}
.hero-title{left:0;top:228px;width:1200px;text-align:center;font-family:var(--serif);font-size:62px;line-height:88px;letter-spacing:3px}
.hero-btn{left:400px;top:446px;width:400px;height:56px;font-size:24px;border:2px solid var(--gold-light)}

/* about */
.about-photo{left:175px;top:968px;width:356px;height:482px;background:linear-gradient(135deg,#8b7a66,#d8cfc0 50%,#5a5048);border:2px solid var(--gold);box-shadow:-8px 8px 0 -4px var(--black),-10px 10px 0 -4px var(--gold)}

/* services */
.service{position:absolute;top:1846px;width:258px;height:365px;background:var(--white);border-radius:0 0 129px 129px;overflow:hidden;text-align:center;color:#2b2b2b}
.service .photo{position:static;width:100%;height:167px}
.service h3{font-family:var(--serif);font-weight:400;font-size:21px;line-height:31px;margin-top:28px;color:#222}
.service p{font-size:13px;line-height:19px;margin:6px 24px 0;color:#444}

/* why */
.reason{position:absolute;width:290px;height:82px}
.reason .icon{position:absolute;left:0;top:6px;width:64px;height:70px;border:2px solid var(--gold);border-radius:4px;box-shadow:0 6px 10px -4px var(--gold)}
.reason h4{position:absolute;left:85px;top:0;font-family:var(--serif);font-weight:400;font-size:19px;letter-spacing:.5px}
.reason p{position:absolute;left:85px;top:32px;font-size:12px;line-height:18px;color:var(--grey);width:205px}

/* team */
.member{position:absolute;top:3371px;width:253px;text-align:center}
.member .photo{position:static;width:253px;height:268px;border-radius:60px 0 60px 0}
.member h4{font-family:var(--serif);font-weight:400;font-size:24px;margin-top:34px}
.member p{font-size:13px;line-height:24px;color:var(--grey);margin-top:6px}
.dots{left:570px;top:3787px;display:flex;gap:8px}
.dots i{width:13px;height:13px;border-radius:50%;background:var(--gold)}
.dots i:first-child{background:var(--white)}

/* blog */
.post{left:170px;top:4168px;width:405px;height:427px;border:2px solid var(--white);border-radius:18px;overflow:hidden}
.post .photo{position:static;width:100%;height:214px}
.post .meta{position:absolute;left:30px;top:242px;right:22px;display:flex;justify-content:space-between;font-size:16px;color:var(--gold-light)}
.post .meta b{font-weight:400;font-size:13px;font-family:var(--serif)}
.post h4{position:absolute;left:30px;top:278px;font-family:var(--serif);font-weight:400;font-size:19px;line-height:28px;letter-spacing:.5px}
.post p{position:absolute;left:30px;top:340px;width:340px;font-size:13px;line-height:19px;color:var(--grey)}
.brief{position:absolute;left:621px;width:404px;height:129px;border:2px solid var(--white);border-radius:16px}
.brief .date{position:absolute;left:26px;top:18px;font-family:var(--serif);font-size:34px;line-height:40px;color:var(--gold)}
.brief h5{position:absolute;left:98px;top:18px;font-family:var(--serif);font-weight:400;font-size:12px;line-height:27px}
.brief p{position:absolute;left:94px;top:76px;width:290px;font-size:10px;line-height:17px;color:var(--grey)}

/* footer */
.footer-band{left:0;top:4640px;width:1200px;height:471px}
.footer-brand{left:165px;top:4790px;width:200px;text-align:center;font-family:var(--serif);font-size:20px;color:#1a1205;line-height:28px}
.footer-brand .mark{display:block;margin:0 auto 8px;width:40px;height:40px;border:2px solid #1a1205}
.footer-social{left:183px;top:4904px;display:flex;gap:18px}
.footer-social i{width:36px;height:36px;border-radius:50%;background:var(--black)}
.footer h4{position:absolute;font-family:var(--serif);font-weight:400;font-size:24px;color:#1a1205}
.links{left:487px;top:4828px;list-style:none;font-size:13px;line-height:31px;color:#1a1205}
.contact-row{position:absolute;left:777px;display:flex;align-items:center;gap:18px;color:#1a1205}
.copyright{left:0;top:5042px;width:1200px;text-align:center;font-family:var(--serif);font-size:11px;color:#1a1205;letter-spacing:.5px}
.footer-line{left:160px;top:5028px;width:880px;height:1px;background:#6a5226}
</style>
</head>
<body>

<!-- Hero -->
<div class="photo hero-photo" role="img" aria-label="Businesswoman in glasses working on a laptop in a dim office"></div>
<div class="abs hero-fade"></div>

<header>
  <div class="abs brand"><span class="mark"></span>KESTWELL FINANZ AG</div>
  <div class="abs topbar">
    <svg width="26" height="26" viewBox="0 0 24 24"><path d="M6.6 10.8a15 15 0 0 0 6.6 6.6l2.2-2.2c.3-.3.7-.4 1-.2 1.1.4 2.3.6 3.6.6.6 0 1 .4 1 1V20c0 .6-.4 1-1 1A17 17 0 0 1 3 4c0-.6.4-1 1-1h3.5c.6 0 1 .4 1 1 0 1.3.2 2.5.6 3.6.1.3 0 .7-.2 1z" fill="none" stroke="#fff" stroke-width="1.6"/></svg>
    <span>044 555 0192</span>
    <div class="social" style="margin-left:22px"><i></i><i></i><i></i></div>
  </div>
  <nav class="abs nav">
    <a class="active">HOME</a><a>ABOUT US</a><a>SERVICES</a><a>OUR TEAM</a><a>BLOG</a><a>CONTACT US</a>
  </nav>
</header>

<h1 class="abs hero-title" style="font-weight:400">WELCOME&nbsp; TO<br>KESTWELL FINANZ</h1>
<a class="btn hero-btn">INTEREST RATE CALCULATOR</a>

<!-- About -->
<section>
  <div class="photo about-photo" role="img" aria-label="Team meeting around a table with charts and coffee"></div>
  <h2 class="heading" style="left:600px;top:952px;font-size:60px;font-weight:400">ABOUT US</h2>
  <div class="rule" style="left:620px;top:1020px;width:220px"><span></span><span></span></div>
  <p class="lede" style="left:599px;top:1054px;width:432px;font-size:15px;color:var(--white)">Lorem ipsum dolor sit amet, consectetur adipiscing elit, sed do eiusmod tempor incididunt ut labore et dolore magna aliqua. Ut enim ad minim veniam, quis nostrud exercitation ullamco laboris nisi ut aliquip ex ea commodo consequat. Duis aute irure dolor in reprehenderit in voluptate velit esse cillum dolore eu fugiat nulla pariatur. Excepteur sint occaecat cupidatat non proident, sunt in culpa qui officia deserunt mollit anim id est laborum.Lorem ipsum dolor sit amet, consectetur adipiscing elit, sed do eiusmod tempor incididunt ut labore et dolore magna aliqua. Ut enim ad minim veniam, quis nostrud exercitation ullamco laboris nisi ut aliquip ex ea commodo consequat.</p>
  <a class="btn" style="left:600px;top:1388px;width:197px;height:48px;font-size:22px">READ MORE</a>
</section>

<!-- Services band -->
<svg class="abs" style="left:0;top:1455px" width="1200" height="992" viewBox="0 0 1200 992">
  <polygon points="0,82 1200,0 1200,895 0,988" fill="#1b1b1b"/>
</svg>
<section>
  <h2 class="heading" style="left:170px;top:1614px;font-weight:400">OUR SERVICES</h2>
  <div class="rule" style="left:210px;top:1690px;width:400px"><span></span><span></span></div>
  <p class="lede" style="left:175px;top:1745px;width:780px">Lorem ipsum dolor sit amet, consectetur adipiscing elit, sed do eiusmod tempor incididunt ut labore et dolore magna aliqua. Ut enim ad minim veniam, commodo consequat.</p>
  <article class="service" style="left:170px"><div class="photo" style="background:linear-gradient(135deg,#3b4656,#9aa3ad)" role="img" aria-label="Colleagues reviewing investment charts on screens"></div><h3>INVESTMENT<br>PLANNING</h3><p>Lorem ipsum dolor sit amet, consectetur adipiscing elit, magna aliqua.</p></article>
  <article class="service" style="left:470px"><div class="photo" style="background:linear-gradient(135deg,#c9ccd2,#6d7a90)" role="img" aria-label="Hands beside a laptop showing a bar chart"></div><h3>FINANCIAL<br>PLANNING</h3><p>Lorem ipsum dolor sit amet, consectetur adipiscing elit, magna aliqua.</p></article>
  <article class="service" style="left:771px"><div class="photo" style="background:linear-gradient(135deg,#2c3442,#a0886a)" role="img" aria-label="Advisors shaking hands over documents"></div><h3>TAX &amp; ESTATE<br>PLANNING</h3><p>Lorem ipsum dolor sit amet, consectetur adipiscing elit, magna aliqua.</p></article>
  <a class="btn" style="left:502px;top:2262px;width:196px;height:46px;font-size:22px">VIEW MORE</a>
</section>

<!-- Why choose -->
<section>
  <h2 class="heading" style="left:0;top:2490px;width:1200px;text-align:center;font-weight:400">WHY CHOOSE US?</h2>
  <div class="rule" style="left:340px;top:2580px;width:520px"><span></span><span></span></div>
  <div class="reason" style="left:163px;top:2675px"><div class="icon"><svg width="60" height="66" viewBox="0 0 60 66"><circle cx="30" cy="28" r="10" fill="var(--gold)"/><rect x="25" y="39" width="10" height="8" fill="var(--gold)"/></svg></div><h4>LOREM IPSUM</h4><p>Lorem ipsum dolor sit amet, consectetur adipiscing elit, magna aliqua.</p></div>
  <div class="reason" style="left:478px;top:2675px"><div class="icon"><svg width="60" height="66" viewBox="0 0 60 66"><rect x="19" y="18" width="22" height="30" fill="none" stroke="var(--gold)" stroke-width="3"/><path d="M24 27h12M24 33h12M24 39h8" stroke="var(--gold)" stroke-width="2"/></svg></div><h4>LOREM IPSUM</h4><p>Lorem ipsum dolor sit amet, consectetur adipiscing elit, magna aliqua.</p></div>
  <div class="reason" style="left:795px;top:2675px"><div class="icon"><svg width="60" height="66" viewBox="0 0 60 66"><circle cx="30" cy="33" r="12" fill="none" stroke="var(--gold)" stroke-width="3"/><text x="30" y="39" text-anchor="middle" font-family="Poppins,sans-serif" font-size="16" fill="var(--gold)">$</text></svg></div><h4>LOREM IPSUM</h4><p>Lorem ipsum dolor sit amet, consectetur adipiscing elit, magna aliqua.</p></div>
  <div class="reason" style="left:163px;top:2864px"><div class="icon"><svg width="60" height="66" viewBox="0 0 60 66"><path d="M30 18l12 5v9c0 8-5 13-12 16-7-3-12-8-12-16v-9z" fill="none" stroke="var(--gold)" stroke-width="3"/><rect x="26" y="30" width="8" height="7" fill="var(--gold)"/></svg></div><h4>LOREM IPSUM</h4><p>Lorem ipsum dolor sit amet, consectetur adipiscing elit, magna aliqua.</p></div>
  <div class="reason" style="left:478px;top:2864px"><div class="icon"><svg width="60" height="66" viewBox="0 0 60 66"><path d="M20 30h6v16h-6zM28 30l5-10c3 0 4 2 3 5l-1 4h7c2 0 3 2 2 4l-3 11c-1 2-2 2-4 2H28z" fill="var(--gold)"/></svg></div><h4>LOREM IPSUM</h4><p>Lorem ipsum dolor sit amet, consectetur adipiscing elit, magna aliqua.</p></div>
  <div class="reason" style="left:795px;top:2864px"><div class="icon"><svg width="60" height="66" viewBox="0 0 60 66"><circle cx="30" cy="33" r="13" fill="var(--gold)"/><text x="30" y="39" text-anchor="middle" font-family="Poppins,sans-serif" font-size="16" fill="#060606">$</text></svg></div><h4>LOREM IPSUM</h4><p>Lorem ipsum dolor sit amet, consectetur adipiscing elit, magna aliqua.</p></div>
  <a class="btn" style="left:502px;top:2998px;width:196px;height:46px;font-size:22px">VIEW MORE</a>
</section>

<!-- Team band -->
<svg class="abs" style="left:0;top:3075px" width="1200" height="832" viewBox="0 0 1200 832">
  <polygon points="0,90 1200,0 1200,760 0,828" fill="#1b1b1b"/>
</svg>
<section>
  <h2 class="heading" style="left:0;top:3168px;width:1024px;text-align:right;font-weight:400">OUR TEAM</h2>
  <div class="rule" style="left:704px;top:3252px;width:320px"><span></span><span></span></div>
  <p class="lede" style="left:250px;top:3292px;width:776px;text-align:right">Lorem ipsum dolor sit amet, consectetur adipiscing elit, sed do eiusmod tempor incididunt ut labore et dolore magna aliqua. Ut enim ad minim veniam, commodo consequat.</p>
  <div class="member" style="left:170px"><div class="photo" style="background:linear-gradient(160deg,#cfd6de,#4a4e57)" role="img" aria-label="Portrait of a smiling advisor in a grey suit"></div><h4>LUKAS BRENNER</h4><p>Lorem ipsum dolor sit amet, c<br>labore et dolore magna aliqua.</p></div>
  <div class="member" style="left:472px"><div class="photo" style="background:linear-gradient(160deg,#e6e4e0,#1f2e4a)" role="img" aria-label="Portrait of a smiling advisor in a navy blazer"></div><h4>MARA KELLER</h4><p>Lorem ipsum dolor sit amet, c<br>labore et dolore magna aliqua.</p></div>
  <div class="member" style="left:773px"><div class="photo" style="background:linear-gradient(160deg,#8b9098,#1b1d22)" role="img" aria-label="Portrait of a smiling advisor in a dark suit"></div><h4>JONAS VOGT</h4><p>Lorem ipsum dolor sit amet, c<br>labore et dolore magna aliqua.</p></div>
  <div class="abs dots"><i></i><i></i><i></i></div>
</section>

<!-- Blog -->
<section>
  <h2 class="heading" style="left:175px;top:3954px;font-weight:400">LATEST BLOG</h2>
  <div class="rule" style="left:205px;top:4038px;width:380px"><span></span><span></span></div>
  <p class="lede" style="left:175px;top:4080px;width:780px">Lorem ipsum dolor sit amet, consectetur adipiscing elit, sed do eiusmod tempor incididunt ut labore et dolore magna aliqua. Ut enim ad minim veniam, commodo consequat.</p>
  <article class="abs post">
    <div class="photo" style="background:linear-gradient(135deg,#d9d6d2,#3c3a3a)" role="img" aria-label="Advisors in a meeting with a client"></div>
    <div class="meta"><span>12.01.2022</span><span><b>&#9650; LIKES</b>&nbsp;&nbsp;&nbsp;<b>&#9679; TWEETS</b></span></div>
    <h4>LOREM IPSUM DOLOR SIT AMET,<br>CONSECTETUR&nbsp; FACILISIS.</h4>
    <p>Lorem ipsum dolor sit amet, consectetur adipiscing elit, sed do eiusmod tempor ut labore et dolore magna aliqua.</p>
  </article>
  <article class="brief" style="top:4168px"><div class="date">02<br>FEB</div><h5>LOREM IPSUM DOLOR SIT AMET,<br>CONSECTETUR&nbsp; FACILISIS.</h5><p>Lorem ipsum dolor sit amet, consectetur adipiscing o eiusmod tempor ut labore et dolore magna aliqua.</p></article>
  <article class="brief" style="top:4319px"><div class="date">02<br>FEB</div><h5>LOREM IPSUM DOLOR SIT AMET,<br>CONSECTETUR&nbsp; FACILISIS.</h5><p>Lorem ipsum dolor sit amet, consectetur adipiscing o eiusmod tempor ut labore et dolore magna aliqua.</p></article>
  <article class="brief" style="top:4468px"><div class="date">02<br>FEB</div><h5>LOREM IPSUM DOLOR SIT AMET,<br>CONSECTETUR&nbsp; FACILISIS.</h5><p>Lorem ipsum dolor sit amet, consectetur adipiscing o eiusmod tempor ut labore et dolore magna aliqua.</p></article>
</section>

<!-- Footer -->
<footer class="footer">
  <svg class="abs footer-band" viewBox="0 0 1200 471" preserveAspectRatio="none">
    <defs><linearGradient id="footerGold" x1="0" y1="0" x2="1" y2="1"><stop offset="0" stop-color="#b8924a"/><stop offset=".5" stop-color="#e6c98a"/><stop offset="1" stop-color="#c9a560"/></linearGradient></defs>
    <polygon points="0,110 1200,0 1200,471 0,471" fill="url(#footerGold)"/>
  </svg>
  <div class="abs footer-brand"><span class="mark"></span>KESTWELL FINANZ AG</div>
  <div class="abs footer-social"><i></i><i></i><i></i></div>
  <h4 style="left:480px;top:4772px">QUICK LINKS</h4>
  <ul class="abs links"><li>HOME</li><li>ABOUT US</li><li>SERVICES</li><li>OUR TEAM</li><li>BLOG</li><li>CONTACT US</li></ul>
  <h4 style="left:777px;top:4772px">CONTACT US</h4>
  <div class="contact-row" style="top:4826px;font-size:14px;line-height:18px"><svg width="30" height="38" viewBox="0 0 24 30"><path d="M12 2a9 9 0 0 0-9 9c0 7 9 17 9 17s9-10 9-17a9 9 0 0 0-9-9z" fill="none" stroke="#1a1205" stroke-width="2"/><circle cx="12" cy="11" r="3.5" fill="none" stroke="#1a1205" stroke-width="2"/></svg><span>Lorem ipsum dolor sit<br>amet, consectetur<br>magna aliqua.</span></div>
  <div class="contact-row" style="top:4918px;font-size:20px"><svg width="32" height="32" viewBox="0 0 24 24"><path d="M6.6 10.8a15 15 0 0 0 6.6 6.6l2.2-2.2c.3-.3.7-.4 1-.2 1.1.4 2.3.6 3.6.6.6 0 1 .4 1 1V20c0 .6-.4 1-1 1A17 17 0 0 1 3 4c0-.6.4-1 1-1h3.5c.6 0 1 .4 1 1 0 1.3.2 2.5.6 3.6.1.3 0 .7-.2 1z" fill="none" stroke="#1a1205" stroke-width="2"/></svg><span>044 555 0192</span></div>
  <div class="contact-row" style="top:4986px;font-size:15px"><svg width="32" height="30" viewBox="0 0 24 22"><rect x="2" y="4" width="20" height="15" fill="none" stroke="#1a1205" stroke-width="2"/><path d="M2 5l10 8 10-8" fill="none" stroke="#1a1205" stroke-width="2"/></svg><span>info@kestwellfinanz.ch</span></div>
  <div class="abs footer-line"></div>
  <p class="abs copyright">COPY RIGHT © 2022 KESTWELL FINANZ&nbsp; I ALL RIGHTS RESERVED</p>
</footer>

</body>
</html>
```